Management consulting Company in the electronic payment ecosystem needs a Website

We need to have a "showcase" style website that contains the key message that our company is able to provide management consulting in the world of payment systems. Our mission is to assist our clients in reviewing their sales, purchasing, operation and IT processes and to support them in identifying the best solution in the use of payment systems.

```html
<!DOCTYPE html>
<html lang="en">
<head>
<meta charset="utf-8">
<title>Veltro Consulting – Payment Systems Consulting</title>
<link href="https://fonts.googleapis.com/css2?family=Poppins:wght@400;500;600&display=swap" rel="stylesheet">
<style>
:root{
  --navy:#0e1a63;
  --navy-deep:#0a1550;
  --bright:#1f3bb3;
  --white:#ffffff;
  --ink:#0e1a63;
  --text:#2b3370;
  --photo-a:#2d3f8c;
  --photo-b:#8aa7d8;
}
*{margin:0;padding:0;box-sizing:border-box}
html,body{width:1200px;height:4549px;overflow:hidden}
body{font-family:'Poppins',sans-serif;color:var(--text);background:var(--white);position:relative}
.abs{position:absolute}
.section{position:absolute;left:0;width:1200px;overflow:hidden}
.navy{background:var(--navy);color:var(--white)}
.btn{position:absolute;border:1.5px solid currentColor;border-radius:20px;font-size:11px;display:flex;align-items:center;justify-content:center}
.btn-solid{background:var(--white);color:var(--navy);border-color:var(--white)}
.brand{display:flex;align-items:center;gap:8px;font-weight:600;font-size:34px;color:var(--white)}
.brand-dot{width:40px;height:40px;border-radius:50%;border:4px solid var(--white)}
.nav{position:absolute;top:44px;right:152px;display:flex;gap:32px;font-size:11px;font-weight:500}
.hero-title{left:141px;top:212px;font-size:25px;line-height:32px;font-weight:500;width:420px}
.dots{left:141px;top:318px;display:flex;gap:5px}
.dots span{width:6px;height:6px;border-radius:50%;background:var(--white)}
.hero-copy{left:141px;top:338px;width:375px;font-size:10.5px;line-height:16px}
.para{font-size:12px;line-height:20px}
.h2{font-size:27px;font-weight:600;color:var(--ink)}
.card-title{font-size:16px;line-height:24px;font-weight:500;width:270px}
.card-copy{font-size:12px;line-height:20.5px;width:270px;letter-spacing:.1px}
.stat{text-align:center;width:240px;color:var(--ink)}
.stat b{display:block;font-size:48px;font-weight:400;line-height:54px}
.stat span{font-size:12px}
.feature{text-align:center;width:240px}
.feature h3{font-size:14px;font-weight:500;margin:8px 0 6px}
.feature p{font-size:11px;line-height:17px}
.field{position:absolute;left:143px;width:484px;border:1.5px solid var(--white);border-radius:18px;font-size:11px;padding:0 18px;display:flex;align-items:center}
.foot-h{font-size:12px;font-weight:500}
.foot-l{font-size:9.5px;line-height:19px}
</style>
</head>
<body>

<!-- Hero -->
<header class="section navy" style="top:0;height:676px">
  <svg class="abs" style="left:0;top:0" width="1200" height="676" aria-hidden="false">
    <defs><clipPath id="heroClip"><circle cx="1005" cy="520" r="430"/></clipPath>
      <linearGradient id="heroPhoto" x1="0" y1="0" x2="1" y2="1"><stop offset="0" stop-color="#c98a8a"/><stop offset=".45" stop-color="#4a5f9e"/><stop offset="1" stop-color="#1b2a6e"/></linearGradient></defs>
    <circle cx="995" cy="515" r="470" fill="none" stroke="#ffffff" stroke-width="2"/>
    <rect x="560" y="80" width="640" height="600" fill="url(#heroPhoto)" clip-path="url(#heroClip)" role="img" aria-label="Hand holding a smartphone surrounded by digital payment network icons"/>
  </svg>
  <div class="abs brand" style="left:141px;top:22px"><span class="brand-dot"></span>Veltro</div>
  <nav class="nav"><span>SERVICES</span><span>ABOUT US</span><span>FAQ</span><span>CONTACT US</span></nav>
  <h1 class="abs hero-title">Beyond digital transformations Modernizing core technology for the AI bank of the future</h1>
  <div class="abs dots"><span></span><span></span><span></span></div>
  <p class="abs hero-copy">Lorem ipsum dolor sit amet, consectetur adipiscing elit, sed do eiusmod tempor incididunt ut labore et dolore magna aliqua. Ut enim ad minim veniam, quis nostrud exercitation ullamco laboris nisi ut aliquip ex ea commodo consequat. Duis aute irure dolor in reprehenderit in voluptate velit esse cillum dolore eu fugiat nulla pariatur. Excepteur sint occaecat cupidatat non proident, sunt in culpa qui officia deserunt mollit anim id est laborum.</p>
  <span class="btn" style="left:141px;top:476px;width:118px;height:33px">Learn More</span>
  <span class="btn btn-solid" style="left:277px;top:476px;width:118px;height:33px">Contact Us</span>
  <svg class="abs" style="left:420px;top:484px" width="18" height="14"><path d="M3 4l6 6 6-6" fill="none" stroke="#fff" stroke-width="2.5"/></svg>
</header>

<!-- Insights -->
<section class="section" style="top:676px;height:427px">
  <svg class="abs" style="left:155px;top:30px" width="360" height="360">
    <circle cx="180" cy="180" r="176" fill="none" stroke="var(--navy)" stroke-width="2.5"/>
    <circle cx="180" cy="180" r="164" fill="#4a6aa8" role="img" aria-label="Smiling customer paying online with a card and smartphone"/>
  </svg>
  <h2 class="abs h2" style="left:621px;top:88px">Insights on Financial Services</h2>
  <p class="abs para" style="left:621px;top:134px;width:440px">Lorem ipsum dolor sit amet, consectetur adipiscing elit, sed do eiusmod tempor incididunt ut labore et dolore magna aliqua. Ut enim ad minim veniam, quis nostrud exercitation ullamco laboris nisi ut aliquip ex ea commodo consequat. Duis aute irure dolor in reprehenderit in voluptate velit esse cillum dolore eu fugiat nulla pariatur. Excepteur sint occaecat cupidatat non proident, sunt in culpa qui officia deserunt mollit anim id est laborum.</p>
  <span class="btn" style="left:621px;top:298px;width:119px;height:34px;color:var(--navy)">Learn More</span>
</section>

<!-- Articles -->
<section class="section navy" style="top:1103px;height:653px">
  <svg class="abs" style="left:0;top:70px" width="1200" height="200">
    <g fill="none" stroke="#fff" stroke-width="2">
      <circle cx="265" cy="101" r="94"/><circle cx="600" cy="101" r="94"/><circle cx="927" cy="101" r="94"/>
    </g>
    <circle cx="265" cy="101" r="86" fill="#3d7fc9" role="img" aria-label="Hand with phone showing a payment confirmation"/>
    <circle cx="600" cy="101" r="86" fill="#8c6a3a" role="img" aria-label="Tablet with a glowing shopping cart icon"/>
    <circle cx="927" cy="101" r="86" fill="#b9bcc4" role="img" aria-label="Person typing on a laptop"/>
  </svg>
  <h3 class="abs card-title" style="left:141px;top:277px">Global Insurance Pools statistics and trends: An overview of life, P&amp;C, and health insurance</h3>
  <h3 class="abs card-title" style="left:470px;top:277px;letter-spacing:1px">How insurers can act on the opportunity of digital eco systems</h3>
  <h3 class="abs card-title" style="left:798px;top:277px">Revolutionizing insurance: The personalized insurance engine</h3>
  <p class="abs card-copy" style="left:141px;top:370px">Lorem ipsum dolor sit amet, consectetur adipiscing elit, sed do eiusmod tempor incididunt ut labore et dolore magna aliqua. Ut enim ad minim veniam, quis nostrud exercitation ullamco laboris nisi ut aliquip ex ea commodo consequat.</p>
  <p class="abs card-copy" style="left:470px;top:370px">Lorem ipsum dolor sit amet, consectetur adipiscing elit, sed do eiusmod tempor incididunt ut labore et dolore magna aliqua. Ut enim ad minim veniam, quis nostrud exercitation ullamco laboris nisi ut aliquip ex ea commodo consequat.</p>
  <p class="abs card-copy" style="left:798px;top:370px">Lorem ipsum dolor sit amet, consectetur adipiscing elit, sed do eiusmod tempor incididunt ut labore et dolore magna aliqua. Ut enim ad minim veniam, quis nostrud exercitation ullamco laboris nisi ut aliquip ex ea commodo consequat.</p>
  <span class="btn" style="left:141px;top:512px;width:97px;height:28px">Read More</span>
  <span class="btn" style="left:470px;top:512px;width:97px;height:28px">Read More</span>
  <span class="btn" style="left:798px;top:512px;width:97px;height:28px">Read More</span>
</section>

<!-- Stats -->
<section class="section" style="top:1756px;height:600px">
  <div class="abs stat" style="left:185px;top:44px"><b>135</b><span>Companies helped</span></div>
  <div class="abs stat" style="left:448px;top:44px"><b>60%</b><span>Y.O.Y Growth</span></div>
  <div class="abs stat" style="left:747px;top:44px"><b>2000+</b><span>Professionals in our network</span></div>
  <div class="abs" style="left:447px;top:58px;width:1.5px;height:57px;background:var(--navy)"></div>
  <div class="abs" style="left:704px;top:58px;width:1.5px;height:57px;background:var(--navy)"></div>
  <p class="abs para" style="left:300px;top:150px;width:600px;text-align:center;font-size:11.5px">Lorem ipsum dolor sit amet, consectetur adipiscing elit, sed do eiusmod tempor incididunt ut labore et dolore magna aliqua.</p>
  <span class="btn" style="left:542px;top:214px;width:116px;height:30px;background:var(--navy);color:#fff;border-color:var(--navy)">Contact Us</span>
  <svg class="abs" style="left:0;top:260px" width="1200" height="340">
    <circle cx="600" cy="465" r="441" fill="none" stroke="var(--navy)" stroke-width="2.5"/>
    <circle cx="600" cy="465" r="415" fill="#7a8aa0" role="img" aria-label="Finger tapping payment options on a point-of-sale terminal"/>
  </svg>
</section>

<!-- Features -->
<section class="section navy" style="top:2356px;height:595px">
  <svg class="abs" style="left:0;top:110px" width="1200" height="300" fill="none" stroke="#fff" stroke-width="2.5">
    <g transform="translate(238,0)"><rect x="6" y="4" width="28" height="36"/><path d="M0 42h40M13 12h4M23 12h4M13 20h4M23 20h4M13 28h4M23 28h4M17 42v-8h6v8"/></g>
    <g transform="translate(580,0)"><circle cx="20" cy="22" r="19"/><ellipse cx="20" cy="22" rx="8" ry="19"/><path d="M1 22h38M5 12h30M5 32h30"/></g>
    <g transform="translate(916,0)"><rect x="0" y="6" width="46" height="30"/><path d="M14 44h18M23 36v8"/><rect x="50" y="0" width="14" height="40"/></g>
    <g transform="translate(232,232)"><path d="M2 14L26 2l24 12H2zM4 48h44M8 18v26M18 18v26M34 18v26M44 18v26"/></g>
    <g transform="translate(575,232)"><circle cx="10" cy="10" r="6"/><circle cx="42" cy="12" r="6"/><circle cx="26" cy="38" r="6"/><path d="M16 10h20M13 15l10 18M38 17l-9 16"/></g>
    <g transform="translate(926,222)"><circle cx="26" cy="26" r="24"/><path d="M33 17c-2-3-12-4-13 2s14 4 13 11-13 6-15 1M26 10v32"/></g>
  </svg>
  <div class="abs feature" style="left:138px;top:164px"><h3>Lorem ipsum dolor sit amet</h3><p>Lorem ipsum dolor sit amet, consectetur adipiscing elit, sed do eiusmod tempor incididunt ut labore et dolore magna</p></div>
  <div class="abs feature" style="left:480px;top:164px"><h3>Lorem ipsum dolor sit amet</h3><p>Lorem ipsum dolor sit amet, consectetur adipiscing elit, sed do eiusmod tempor incididunt ut labore et dolore magna</p></div>
  <div class="abs feature" style="left:833px;top:164px"><h3>Lorem ipsum dolor sit amet</h3><p>Lorem ipsum dolor sit amet, consectetur adipiscing elit, sed do eiusmod tempor incididunt ut labore et dolore magna</p></div>
  <div class="abs feature" style="left:138px;top:397px"><h3>Lorem ipsum dolor sit amet</h3><p>Lorem ipsum dolor sit amet, consectetur adipiscing elit, sed do eiusmod tempor incididunt ut labore et dolore magna</p></div>
  <div class="abs feature" style="left:480px;top:397px"><h3>Lorem ipsum dolor sit amet</h3><p>Lorem ipsum dolor sit amet, consectetur adipiscing elit, sed do eiusmod tempor incididunt ut labore et dolore magna</p></div>
  <div class="abs feature" style="left:833px;top:397px"><h3>Lorem ipsum dolor sit amet</h3><p>Lorem ipsum dolor sit amet, consectetur adipiscing elit, sed do eiusmod tempor incididunt ut labore et dolore magna</p></div>
</section>

<!-- Testimonial -->
<section class="section" style="top:2951px;height:318px">
  <div class="abs" style="left:176px;top:18px;font-size:90px;line-height:90px;color:#c8ccd8;font-family:Georgia,serif">&ldquo;</div>
  <div class="abs" style="left:984px;top:150px;font-size:90px;line-height:90px;color:#c8ccd8;font-family:Georgia,serif">&rdquo;</div>
  <h2 class="abs h2" style="left:0;width:1200px;text-align:center;top:76px;font-size:25px">What our clients say</h2>
  <p class="abs" style="left:258px;top:133px;width:684px;text-align:center;font-size:11px;line-height:16.5px">Lorem ipsum dolor sit amet, consectetur adipiscing elit, sed do eiusmod tempor incididunt ut labore et dolore magna aliqua. Ut enim ad minim veniam, quis nostrud exercitation ullamco laboris nisi ut aliquip ex ea commodo consequat. Duis aute irure dolor in reprehenderit in voluptate velit esse cillum dolore eu fugiat nulla pariatur. Excepteur sint occaecat cupidatat non proident, sunt in culpa qui officia deserunt mollit anim id est laborum.</p>
  <div class="abs" style="left:0;width:1200px;text-align:center;top:210px;font-size:12px;font-weight:600;color:var(--ink)">Mara Lindqvist</div>
  <div class="abs" style="left:0;width:1200px;text-align:center;top:228px;font-size:9.5px">His Company Name</div>
</section>

<!-- Contact -->
<section class="section navy" style="top:3269px;height:632px">
  <svg class="abs" style="left:0;top:0" width="1200" height="632">
    <defs><radialGradient id="contactPhoto" cx=".5" cy=".5" r=".6"><stop offset="0" stop-color="#3fb7e8"/><stop offset=".6" stop-color="#2a6fc9"/><stop offset="1" stop-color="#d68ab8"/></radialGradient></defs>
    <circle cx="1060" cy="340" r="355" fill="none" stroke="#fff" stroke-width="2"/>
    <circle cx="1060" cy="340" r="312" fill="url(#contactPhoto)" role="img" aria-label="Finger touching a smartphone with a glowing contact screen and digital icons"/>
  </svg>
  <h2 class="abs" style="left:143px;width:484px;text-align:center;top:78px;font-size:25px;font-weight:500">Contact Us</h2>
  <p class="abs" style="left:213px;width:344px;text-align:center;top:120px;font-size:11px;line-height:17px">Lorem ipsum dolor sit amet, consectetur adipiscing elit sed do eiusmod tempor</p>
  <div class="field" style="top:171px;height:35px">Name</div>
  <div class="field" style="top:222px;height:35px">Email</div>
  <div class="field" style="top:275px;height:35px">Contact Number</div>
  <div class="field" style="top:330px;height:102px;align-items:flex-start;padding-top:16px">Your Message</div>
  <span class="btn btn-solid" style="left:143px;top:457px;width:118px;height:35px;font-size:12px">Submit</span>
  <div class="abs" style="left:143px;width:484px;text-align:center;top:516px;font-size:16px">Call us Today : 0100-55512-0000</div>
  <div class="abs" style="left:143px;width:484px;text-align:center;top:542px;font-size:11.5px">hello@veltro.example</div>
</section>

<!-- Photo band -->
<div class="section" style="top:3901px;height:420px;background:linear-gradient(100deg,#1a2240 0%,#4b5a84 40%,#22306a 70%,#9eb0d6 100%)" role="img" aria-label="Person operating a touchscreen point-of-sale terminal"></div>

<!-- Footer -->
<footer class="section navy" style="top:4321px;height:228px">
  <div class="abs brand" style="left:141px;top:34px;font-size:36px"><span class="brand-dot" style="width:46px;height:46px"></span>Veltro</div>
  <p class="abs" style="left:141px;top:112px;width:160px;font-size:8px;line-height:12px">Lorem ipsum dolor sit amet, consectetur adipiscing elit, sed do eiusmod tempor incididunt ut labore et dolore magna aliqua. Ut enim ad minim veniam, quis nostrud exercitation.</p>
  <div class="abs" style="left:427px;top:30px"><div class="foot-h">Pages</div><div class="foot-l">Services<br>About Us<br>Blog<br>Contact Us</div></div>
  <div class="abs" style="left:618px;top:30px">
    <div class="foot-h">Contact</div>
    <div class="foot-l" style="padding-left:16px;position:relative">
      <svg class="abs" style="left:0;top:4px" width="11" height="72" fill="#fff"><path d="M2 1l3 0 1 3-1.5 1.5a7 7 0 0 0 3 3L9 7l3 1 0 3c-6 0-10-4-10-10z"/><path d="M2 20l3 0 1 3-1.5 1.5a7 7 0 0 0 3 3L9 26l3 1 0 3c-6 0-10-4-10-10z"/><rect x="1" y="40" width="9" height="7" rx="1"/><path d="M5.5 59a3.5 3.5 0 0 1 3.5 3.5c0 2.5-3.5 6-3.5 6s-3.5-3.5-3.5-6A3.5 3.5 0 0 1 5.5 59z"/></svg>
      1300 555 010<br>1300 555 010<br>support@veltro.example<br>Ferrow Lane, Brookfield<br>QLD 4000
    </div>
  </div>
  <svg class="abs" style="left:616px;top:107px" width="90" height="28" fill="none" stroke="#fff" stroke-width="1.5"><circle cx="14" cy="14" r="12"/><circle cx="44" cy="14" r="12"/><circle cx="74" cy="14" r="12"/></svg>
  <div class="abs foot-h" style="left:870px;top:30px">Subscribe to our News Letters</div>
  <div class="field" style="left:865px;width:192px;top:54px;height:31px;justify-content:flex-end;font-size:10px">Name</div>
  <div class="field" style="left:865px;width:192px;top:102px;height:31px;justify-content:flex-end;font-size:10px">Email</div>
  <span class="btn btn-solid" style="left:957px;top:150px;width:100px;height:29px;font-size:10px">Subscribe</span>
  <div class="abs" style="left:0;top:210px;width:1200px;height:18px;background:var(--bright);font-size:8px;text-align:center;line-height:18px">Copyright © 2021 veltroconsulting.example. All Rights Reserved</div>
</footer>

</body>
</html>
```